Ray's Personal Training -> also needs a logo

Services Frankston, Mornington, and Somerville

Specializes in in-home personal training

VimTrek style workouts

Not really preferential colors but needs to look modern and not stock photo

Industry/Entity Type

Training

Requirements
Must have
• 30% off first time customers on a package of 10

```html
<!DOCTYPE html>
<html lang="en">
<head>
<meta charset="utf-8">
<title>Ray's Personal Training</title>
<link rel="stylesheet" href="https://fonts.googleapis.com/css2?family=Source+Sans+3:wght@400;600;700&display=swap">
<style>
  :root {
    --yellow: #fff200;
    --black: #000000;
    --red: #ee1c25;
    --white: #ffffff;
  }
  html, body {
    margin: 0;
    padding: 0;
    overflow: hidden;
  }
  body {
    width: 1200px;
    height: 929px;
    font-family: "Source Sans 3", Arial, sans-serif;
  }
  .flyer {
    position: relative;
    width: 1200px;
    height: 929px;
    background: var(--yellow);
    overflow: hidden;
  }
  .brand-mark {
    position: absolute;
    left: 233px;
    top: 54px;
    width: 190px;
    height: 190px;
    border-radius: 50%;
    background: var(--black);
  }
  .brand-name {
    position: absolute;
    left: 180px;
    top: 240px;
    margin: 0;
    font-size: 128px;
    font-weight: 700;
    line-height: 1;
    color: var(--black);
    letter-spacing: 1px;
  }
  .brand-tagline {
    position: absolute;
    left: 184px;
    top: 375px;
    margin: 0;
    font-size: 46px;
    font-weight: 400;
    line-height: 1;
    color: var(--black);
    letter-spacing: 1px;
  }
  .service-area {
    position: absolute;
    left: 36px;
    top: 455px;
    margin: 0;
    font-size: 30px;
    font-weight: 400;
    color: var(--black);
  }
  .offer-burst {
    position: absolute;
    left: 782px;
    top: 64px;
    width: 420px;
    height: 420px;
  }
  .offer-burst-text {
    position: absolute;
    left: 812px;
    top: 150px;
    width: 360px;
    text-align: center;
    color: var(--white);
    transform: rotate(-20deg);
    line-height: 1.08;
  }
  .offer-burst-text .headline {
    display: block;
    font-size: 62px;
    font-weight: 700;
  }
  .offer-burst-text .detail {
    display: block;
    font-size: 44px;
    font-weight: 400;
  }
  .features {
    position: absolute;
    left: 0;
    top: 506px;
    width: 1200px;
    height: 274px;
    background: var(--black);
    margin: 0;
    padding: 58px 0 0 66px;
    box-sizing: border-box;
    list-style: none;
  }
  .features li {
    color: var(--white);
    font-size: 62px;
    font-weight: 400;
    line-height: 1;
    margin-bottom: 42px;
  }
  .features li::before {
    content: "\2022";
    margin-right: 24px;
  }
  .promo-bar {
    position: absolute;
    left: 0;
    top: 780px;
    width: 1200px;
    height: 149px;
    background: var(--red);
  }
  .promo-bar-text {
    position: absolute;
    left: 54px;
    top: 54px;
    margin: 0;
    font-size: 42px;
    font-weight: 400;
    color: var(--white);
    line-height: 1;
  }
  .promo-bar-mark {
    position: absolute;
    left: 1063px;
    top: 18px;
    width: 96px;
    height: 96px;
    border-radius: 50%;
    background: var(--black);
  }
</style>
</head>
<body>
<main class="flyer">
  <div class="brand-mark" aria-hidden="true"></div>
  <h1 class="brand-name">RAY's</h1>
  <p class="brand-tagline">PERSONAL TRAINING</p>
  <p class="service-area">Services Frankston, Mornington, and Somerville</p>

  <svg class="offer-burst" viewBox="-100 -100 200 200" aria-hidden="true">
    <polygon fill="var(--red)" transform="rotate(4)" points="100,0 87.2,11.5 96.6,25.9 81.3,33.7 86.6,50 69.8,53.6 70.7,70.7 53.6,69.8 50,86.6 33.7,81.3 25.9,96.6 11.5,87.2 0,100 -11.5,87.2 -25.9,96.6 -33.7,81.3 -50,86.6 -53.6,69.8 -70.7,70.7 -69.8,53.6 -86.6,50 -81.3,33.7 -96.6,25.9 -87.2,11.5 -100,0 -87.2,-11.5 -96.6,-25.9 -81.3,-33.7 -86.6,-50 -69.8,-53.6 -70.7,-70.7 -53.6,-69.8 -50,-86.6 -33.7,-81.3 -25.9,-96.6 -11.5,-87.2 0,-100 11.5,-87.2 25.9,-96.6 33.7,-81.3 50,-86.6 53.6,-69.8 70.7,-70.7 69.8,-53.6 86.6,-50 81.3,-33.7 96.6,-25.9 87.2,-11.5"/>
  </svg>
  <div class="offer-burst-text">
    <span class="headline">30% off</span>
    <span class="detail">first time<br>customers on<br>a package<br>of 10</span>
  </div>

  <ul class="features">
    <li>Specializes in in-home personal training</li>
    <li>VimTrek style workouts</li>
  </ul>

  <footer class="promo-bar">
    <p class="promo-bar-text">30% off first time customers on a package of 10</p>
    <div class="promo-bar-mark" aria-hidden="true"></div>
  </footer>
</main>
</body>
</html>
```